Seed & Bloom General Card Design

Please see http://seed-and-bloom.example for more information about our program. In brief, we are a 501(c)(3) nonprofit organization that focuses on improving educational outcomes for all students through parent education and empowerment, K-12 curriculum development, K-12 staff development, learner-oriented live events, community service projects, and more. We are now preparing to launch our Seed & Bloom Educational Series, which is devoted to teaching children and the adults in their lives about making healthy food choices and regaining control over what is in their food by growing it themselves in easy, affordable self-watering container gardens that can be placed in spaces not otherwise suitable for growing fruits and vegetables, such as paved lots and rooftops, are portable, and can be quickly built from recycled materials. In fact, we have local businesses already lining up to donate clean, safe 5-gallon buckets for this initiative (our container design uses 5-gallon buckets). We have already built out content on the site to support as many of the Trail Rangers merit badges as we could tie to the instructional goals of our Seed & Bloom Educational Series. We are in the processes of developing K-12 curricula tied to the Common Core and STEM (science, technology, engineering, & math), which we will be giving away for free under a Creative Commons license to help public schools in states that have recently adopted the Common Core but can't afford to replace all their textbooks and don't have the time to scramble to create curricula of their own. This card will be used by all of our Seed & Bloom staff and volunteers to share out information about the program and promote it to others. It will go out in mailings, sit on display tables at events, be left at kiosks, and be handed out in person. It needs to be color-matched to our Seed & Bloom site. The logo on the site we created for our Seed & Bloom Educational Series was done using an online service and the quality of the image is quite poor (see attached file). When we use it in print materials and then convert them to PDF, the logo becomes pixelated. It's awful. We are not entirely married to keeping the logo if you can come up with something better and we are given the final JPG or PNG file of the logo to upload to the site so they match. If you can just improve the quality of the existing logo, that's fine, too. Please note that the phrase "Seed & Bloom Educational Series" is a service mark of TVR7Families and should be followed by the letters "SM" in superscript at the end of the word "Series" in any logo you create.
Target Market(s)
parents of K-12 students, K-12 teachers, community service organizations, youth organizations, programs for the elderly, programs for the disabled
Industry/Entity Type
Community Service
Contact Information for Business Card
TVR7Families' Seed & Bloom Educational Series, http://seed-and-bloom.example, (555) 214-7389, Non-GMO/Organic Family & Community Gardening Workshops, K-12 Common Core/STEM Curricula Development, Community Service Projects, Online Gardening & Teaching Communities, Project-Based Learning Activities, Youth Leadership Projects, Fun Contests and Prizes, Corporate & Small Business Social Responsibility Programs, K-12 Staff Development, Education Research & Reporting

```html
<!DOCTYPE html>
<html lang="en">
<head>
<meta charset="utf-8">
<title>Seed &amp; Bloom Educational Series – Card Back</title>
<link rel="stylesheet" href="https://fonts.googleapis.com/css2?family=Oswald:wght@600;700&display=swap">
<style>
  :root {
    --kraft: #c8a877;
    --kraft-light: #d4b688;
    --kraft-dark: #b8965f;
    --leaf-green: #2f9a0f;
  }
  html, body {
    margin: 0;
    padding: 0;
    width: 1200px;
    height: 702px;
    overflow: hidden;
  }
  .card-back {
    position: relative;
    width: 1200px;
    height: 702px;
    background:
      radial-gradient(ellipse at 30% 25%, var(--kraft-light) 0%, transparent 55%),
      radial-gradient(ellipse at 75% 80%, var(--kraft-dark) 0%, transparent 60%),
      var(--kraft);
    display: flex;
    align-items: flex-start;
    justify-content: center;
  }
  .program-list {
    list-style: none;
    margin: 0;
    padding: 84px 0 0;
    text-align: center;
    font-family: "Oswald", sans-serif;
    font-weight: 700;
    font-variant: small-caps;
    font-size: 33px;
    line-height: 55.3px;
    letter-spacing: 0.2px;
    color: var(--leaf-green);
    transform: scaleX(0.86);
  }
  .program-list li {
    white-space: nowrap;
  }
</style>
</head>
<body>
  <main class="card-back">
    <ul class="program-list">
      <li>Non-GMO/Organic Family &amp; Community Gardening Workshops</li>
      <li>K-12 Common Core/STEM Curricula Development</li>
      <li>Community Service Projects</li>
      <li>Online Gardening &amp; Teaching Communities</li>
      <li>Project-Based Learning Activities</li>
      <li>Youth Leadership Projects</li>
      <li>Fun Contests and Prizes</li>
      <li>Corporate &amp; Small Business Social Responsibility Programs</li>
      <li>K-12 Staff Development</li>
      <li>Education Research &amp; Reporting</li>
    </ul>
  </main>
</body>
</html>
```